Refresh our Logo and Letterhead!

We would like to see designs with blue, green, teal etc. Our current logo and contact details for the letterhead is attached.
We're a small boutique firm based in Sydney, Australia. We're near the coast and not opposed to coastal images. We practice in property law and have primarily female practitioners, although we don't necessarily need the logo and letterhead to be too feminine. We would like to see designs with blue, green, teal etc. Our current logo and contact details for the letterhead is attached.
We're a small boutique firm based in Sydney, Australia. We're near the coast and not opposed to coastal images. We practice in property law and have primarily female practitioners, although we don't necessarily need the logo and letterhead to be too feminine.

Target Market(s)

Young professionals

Industry/Entity Type

Law Firm

Logo Text

Marwick Legal

Font styles to use
Serif
Sans Serif

Colors
34a7d8
00a990
85acd3
886aae

Requirements
Must have
• The letterhead must have the text in the "contact info" jpg uploaded with the brief.
Nice to have
• We'd like to see some simple, innovating, fresh ideas. A watermark or something interesting in the background would be good.

```html
<!DOCTYPE html>
<html lang="en">
<head>
<meta charset="utf-8">
<title>Marwick Legal – Letterhead</title>
<link rel="stylesheet" href="https://fonts.googleapis.com/css2?family=Montserrat:wght@300;400&family=Roboto:wght@300;400;700&display=swap">
<style>
  :root {
    --bg: #e4e4e6;
    --paper: #f3f3f3;
    --navy: #1f5fa8;
    --blue: #2a6db5;
    --sky: #4fb0e0;
    --sky-light: #5ec4e6;
    --ink: #333;
    --grey: #7a7a7a;
  }
  * { box-sizing: border-box; margin: 0; padding: 0; }
  html, body { width: 1110px; height: 1200px; overflow: hidden; background: var(--bg); }
  .sheet {
    position: absolute; left: 135px; top: 12px;
    width: 840px; height: 1176px;
    background: var(--paper);
    font-family: 'Montserrat', sans-serif;
    color: var(--ink);
  }
  .brand {
    position: absolute; left: 64px; top: 78px;
    display: flex; align-items: center; gap: 10px;
  }
  .brand-mark { width: 16px; height: 16px; border-radius: 50%; background: var(--navy); }
  .brand-name {
    font-family: 'Montserrat', sans-serif; font-weight: 300;
    font-size: 40px; color: var(--navy); letter-spacing: 0.5px;
  }
  .contact {
    position: absolute; left: 600px; top: 34px;
    font-family: 'Roboto', sans-serif; font-weight: 300;
    font-size: 14px; line-height: 17px; color: var(--navy);
  }
  .contact .address { margin-bottom: 4px; }
  .contact li { list-style: none; display: flex; align-items: center; gap: 6px; }
  .contact svg { width: 10px; height: 10px; fill: var(--sky); flex: none; }
  .header-rule {
    position: absolute; left: 60px; top: 148px;
    width: 720px; height: 2px; background: var(--navy);
  }
  .recipient { position: absolute; left: 86px; top: 262px; }
  .recipient .to { font-size: 14px; letter-spacing: 2px; margin-bottom: 5px; }
  .recipient .name { font-size: 14.5px; color: var(--sky); margin-bottom: 6px; }
  .recipient .line { font-size: 11.5px; color: var(--grey); line-height: 18.5px; }
  .date { position: absolute; right: 85px; top: 266px; font-size: 11.5px; color: #444; }
  .body {
    position: absolute; left: 86px; top: 420px; width: 671px;
    font-size: 12px; line-height: 14.8px; color: var(--grey);
    text-align: justify;
  }
  .body p { margin-bottom: 14.8px; }
  .signature-mark {
    position: absolute; left: 86px; top: 834px;
    width: 143px; height: 32px; border-radius: 4px;
    background: linear-gradient(90deg, #d9d9db, #e6e6e8);
  }
  .signatory { position: absolute; left: 84px; top: 874px; }
  .signatory .name { font-size: 14px; color: #333; }
  .signatory .role { font-size: 11px; color: var(--grey); margin-top: 2px; }
  .footer {
    position: absolute; left: 0; right: 0; top: 1114px;
    text-align: center; font-family: 'Roboto', sans-serif;
  }
  .footer .registration { font-size: 14px; font-weight: 300; color: var(--blue); }
  .footer .registration .sep { margin: 0 8px; }
  .footer .legal { font-size: 9.7px; font-weight: 700; color: var(--navy); margin-top: 8px; }
  .footer-band {
    position: absolute; left: 0; bottom: 0; width: 100%; height: 10px;
    background: linear-gradient(90deg, var(--navy), var(--sky-light));
  }
</style>
</head>
<body>
<main class="sheet">
  <div class="brand">
    <span class="brand-mark"></span>
    <span class="brand-name">Marwick Legal</span>
  </div>

  <address class="contact">
    <div class="address">Po Box 214<br>Seacliff Nsw 2263</div>
    <ul>
      <li><svg viewBox="0 0 10 10"><path d="M2 0.5 L3.8 2.6 L2.9 3.8 Q4 6 6.2 7.1 L7.4 6.2 L9.5 8 L8.3 9.5 Q2.5 9 0.5 1.7 Z"/></svg>02 4391 2068</li>
      <li><svg viewBox="0 0 10 10"><rect x="2.5" y="0.5" width="5" height="9" rx="1"/><rect x="3.4" y="1.6" width="3.2" height="5.8" fill="#f3f3f3"/></svg>0431 508 126</li>
      <li><svg viewBox="0 0 10 10"><rect x="2.5" y="0.5" width="5" height="3"/><rect x="0.5" y="3.5" width="9" height="4" rx="1"/><rect x="2.5" y="6.5" width="5" height="3"/></svg>02 8145 6620</li>
      <li><svg viewBox="0 0 10 10"><rect x="0.5" y="2" width="9" height="6"/><path d="M0.5 2 L5 5.5 L9.5 2" stroke="#f3f3f3" stroke-width="0.9" fill="none"/></svg>hello@marwicklegal.com.au</li>
    </ul>
  </address>

  <div class="header-rule"></div>

  <section class="recipient">
    <div class="to">TO</div>
    <div class="name">Daniel Feroze</div>
    <div class="line">Human Resources</div>
    <div class="line">Northline Inc.</div>
    <div class="line">2207-B Calder Row, Brenton</div>
    <div class="line">K42 USA</div>
  </section>

  <div class="date">Friday, 01/01/2018</div>

  <article class="body">
    <p>Lorem ipsum dolor sit amet, consectetuer adipiscing elit, sed diam nonmmy nibh euismod tincidunt ut laoreet dolore magna aliquam erat volutpat. Ut wisi enim ad minim veniam, quis nostrud exerci tationmcorper suscipit lobortis nisl ut aliquip ex ea commodo consequat. Duis autem vel eum iriure dolor in hendrerit in vulputate velit esse molestie consequat, vel illum dolore eu feugiat nulla facilisis at vero eros et accumsan et iusto odio dignissim qui blandit praesent luptatum zzril delenit augue duis dolore te feugait nulla facilisi.</p>
    <p>Nam liber tempor cum soluta nobis eleifend option congue nihil imprdiet doming id quod mazim placerat facer possim assum. Typi non habent claritatem insitam;</p>
    <p>Est usus legentis in iis qui facit eorum claritatem.</p>
    <p>Investigationes demonstraverunt lectores legere me lius quod ii legunt saepius. Claritas est etiam processus dynamicus, qui sequitur mutationem consuetudium lectorum. Mirum est notare quam littera gothica, quam nunc putamus parum claram, anteposuerit litterarum formas humanitatis per seacula quarta decima et quinta decima. Eodem modo typi, qui nunc nobis videntur parum clari, fiant sollemnes in futurum.</p>
    <p>consectetuer adipiscing elit, sed diam nonummy nibh euismod tincidunt ut laoreet dolore magna aliquam erat volutpat. Ut wisi enim ad minim veniam, quis nostrud exerci tation ullamcorper suscipit lobortis nisl ut aliquip ex ea commodo consequat. Duis autem vel eum iriure dolor in hendrerit in vulputate velit esse molestie consequat, vel illum dolore eu feugiat nulla facilisis at vero eros et accumsan et iusto odio dignissim qui blandit praesent luptatum zzril delenit augue duis dolore te feugait nulla facilisi.</p>
    <p>Nam liber tempor cum soluta nobis eleifend option congue nihil imperdiet .</p>
  </article>

  <div class="signature-mark" role="img" aria-label="Handwritten signature of the managing director"></div>
  <div class="signatory">
    <div class="name">Peter Lanford</div>
    <div class="role">Managing Director</div>
  </div>

  <footer class="footer">
    <div class="registration">ABN: 51 732 094 618<span class="sep">|</span>12 Harbourview Lane, Seacliff Nsw 2263</div>
    <div class="legal">An Incorporated Legal Practice Under The Legal Profession Act 2004 As Amended Liability By A Scheme Approved Under Professional Standards Legislation.</div>
  </footer>
  <div class="footer-band"></div>
</main>
</body>
</html>
```